依頼詳細
依頼は、月刊誌「射心」の裏表紙デザインをお願い致します。弓道されている一般の方は、必ず目にする雑誌です。サイズは【左右154mm×天地232mm】です。尚、2018年10月号(10月1日発刊)に掲載予定です。

当社製品をメインに、シンプルかつ高級感のあるデザインを希望致します。
なんとなくあるイメージは、雑誌によく掲載されているハイブランドの広告のような物を想像していますが、それにとらわれず斬新なものでもかまいません。
ご参考に弊社ホームページをご覧下さい。

今回は「製品紹介」広告ではありませんので、あくまでも企業イメージの浸透をテーマに製作をお願い致します。

尚、素材はフェイスブックhttps://www.facebook.com/ayaseshagu-example/の写真から使用してください。

よろしくお願い致します。
記載項目
社名:有限会社 綾瀬射具工房
住所:〒810-0999 福岡市南区桜台7-14-3
電話番号:092-000-4137
FAX:092-000-4138
URL:http://www.ayaseshagu-example.com/
東洋射芸用品協会会員
弊社ロゴ
「初心者用から特註高級品まで」
希望イメージ
シンプル 複雑
単色 カラフル
暗い 明るい
日常 高級
遊び心 厳粛
未来的 伝統的
女性的 男性的
希望する色
納品ファイル
• イラストレーター形式 (.ai)
補足説明
納品物は
・イラストレータデータ(アウトライン済)
・jpgデータ

尚、採用されたデザインの著作権などの権利は、当社に帰属するようにお願致します。
過去当選作品を掲示させていただきます。ご参考になれば幸いです。
使用する写真についてのご指摘がありましたので、再度共有サイトにアップいたしました。こちらからご利用下さい。

http://photoshare-example.jp/ayaseshagu/1
■ 選んだ理由

構図、ロゴの配置、キャッチフレーズ等、弊社の要望であります「ハイブランド」をうまく体現した作品として、社内投票で1位となりました。

■ 提案者全員のお礼・コメント

前回に引き続き今回の募集でもたくさんの御応募いただきまして真にありがとうございます。

今回の作品もすべて秀逸で、色々考えてこられた作品でしたので、社内投票でもかなり票が割れました。今後もデザイン募集いたしますので、お見かけいただいた際は是非ご参加いただければありがたいです。

```html
<!DOCTYPE html>
<html lang="ja">
<head>
<meta charset="utf-8">
<title>綾瀬射具工房 企業広告</title>
<link rel="stylesheet" href="https://fonts.googleapis.com/css2?family=Shippori+Mincho:wght@400;600;800&display=swap">
<style>
  :root {
    --paper: #ffffff;
    --indigo: #1c2350;
    --indigo-deep: #141a3e;
    --wave-violet: #3d3f7e;
    --ink: #2a2a2a;
    --accent-red: #a3362f;
    --mist-green: #dcefe4;
    --sand: #f1e6d2;
    --glove-brown: #8a5a36;
    --glove-tan: #c9a27a;
  }
  * { margin: 0; padding: 0; box-sizing: border-box; }
  html, body { width: 804px; height: 1200px; overflow: hidden; background: var(--paper); }
  .ad {
    position: relative;
    width: 804px;
    height: 1200px;
    background: var(--paper);
    font-family: "Shippori Mincho", serif;
    color: var(--ink);
    overflow: hidden;
  }
  .indigo-band {
    position: absolute;
    left: 0; top: 0;
    width: 255px; height: 1200px;
    background: linear-gradient(180deg, var(--indigo) 0%, var(--indigo-deep) 100%);
  }
  .wave-field {
    position: absolute;
    left: 0; top: 860px;
    width: 255px; height: 280px;
    background: radial-gradient(ellipse at 40% 60%, var(--wave-violet) 0%, rgba(61,63,126,0.35) 55%, rgba(28,35,80,0) 80%);
  }
  .mist-circle {
    position: absolute;
    left: 470px; top: 195px;
    width: 110px; height: 110px;
    border-radius: 50%;
    background: var(--mist-green);
    opacity: 0.85;
  }
  .sand-circle {
    position: absolute;
    left: 386px; top: 385px;
    width: 72px; height: 72px;
    border-radius: 50%;
    background: var(--sand);
  }
  .motto {
    position: absolute;
    z-index: 2;
    left: 398px; top: 95px;
    writing-mode: vertical-rl;
    font-size: 40px;
    line-height: 1;
    font-weight: 600;
    letter-spacing: 14px;
    color: var(--ink);
  }
  .motto .accent { color: var(--accent-red); }
  .product-photo {
    position: absolute;
    z-index: 1;
    left: 50px; top: 480px;
    width: 690px; height: 350px;
    border-radius: 45% 40% 45% 40% / 40% 45% 45% 50%;
    background: radial-gradient(ellipse at 55% 55%, var(--glove-brown) 0%, var(--glove-tan) 60%, rgba(255,255,255,0) 78%);
  }
  .signature {
    position: absolute;
    left: 300px; right: 0; top: 845px;
    text-align: center;
  }
  .tagline { font-size: 13px; letter-spacing: 2px; }
  .brand-mark {
    display: flex; align-items: center; justify-content: center;
    gap: 12px; margin: 8px 0 10px;
  }
  .brand-dot { width: 64px; height: 64px; border-radius: 50%; border: 3px solid var(--ink); }
  .brand-name { font-size: 20px; font-weight: 600; letter-spacing: 3px; }
  .company { font-size: 24px; font-weight: 800; letter-spacing: 3px; margin-bottom: 8px; }
  .contact { font-size: 13px; line-height: 1.55; letter-spacing: 1px; }
  .membership { font-size: 12px; margin-top: 6px; letter-spacing: 1px; }
</style>
</head>
<body>
<main class="ad">
  <div class="indigo-band"></div>
  <div class="wave-field" role="img" aria-label="藍地に流れる波の文様"></div>
  <div class="mist-circle"></div>
  <div class="sand-circle"></div>
  <h1 class="motto">心・技・体、<span class="accent">美</span></h1>
  <div class="product-photo" role="img" aria-label="刺繍入りの弓懸(ゆがけ)と巻かれた弦の製品写真"></div>
  <section class="signature">
    <p class="tagline">初心者用から特註高級品まで</p>
    <div class="brand-mark">
      <span class="brand-dot"></span>
      <span class="brand-name">綾瀬射具工房</span>
    </div>
    <p class="company">有限会社 綾瀬射具工房</p>
    <p class="contact">〒810-0999 福岡市南区桜台7-14-3<br>
      電話 092-000-4137　FAX 092-000-4138<br>
      http://www.ayaseshagu-example.com/</p>
    <p class="membership">(東洋射芸用品協会会員)</p>
  </section>
</main>
</body>
</html>
```